Postcard Design

Name of the Company is : Harbor Lantern Sport Fishing Charters Block Island RI
Name of the boat : Reel Tide Joy
local Captain Dennis Hartwell
pricing and booking : 401-555-0193
We specialize in:

Shark & Tuna Trips
Full or half day Inshore Bass & Bluefish
Half day bottom fishing for Fluke, Sea Bass & Scup
Inshore night fishing trips
Custom Combination Charters also available
Our crew provides:
A professional and accommodating experience
A very child friendly environment
A range of technique options for every style of trip
An immense knowledge of the waters.
Our Vessel:
Meets all NMSA safety requirement
Twin 250 Hp Valdrek Turbo Diesels
All updated electronics
On the comfort side : we have a restroom, and a galley area with a table so you can enjoy your lunch.

Payments : We except; Cash , Check , Kp, Tz, Rl and Nb

I have attached the logo I would like to use . If possible I would like to use the banners on the logo with Company Name & number.

```html
<!DOCTYPE html>
<html lang="en">
<head>
<meta charset="utf-8">
<title>Harbor Lantern Sport Fishing Charters – Postcard</title>
<link rel="stylesheet" href="https://fonts.googleapis.com/css2?family=Roboto+Condensed:wght@400;700&family=Source+Sans+3:wght@400;700&family=PT+Sans+Narrow:wght@400;700&display=swap">
<style>
  :root {
    --backdrop: #e9e4dc;
    --sea-blue: #2f5fb3;
    --sea-blue-deep: #1f4a98;
    --navy: #1b2f5e;
    --navy-text: #1d3566;
    --gold: #f4b41a;
    --rope: #c9a25a;
    --white: #ffffff;
    --alert-red: #e0231c;
    --photo-sky: #9cc3e6;
    --photo-sea: #3f78b8;
    --photo-warm: #b49a7f;
  }
  * { box-sizing: border-box; margin: 0; padding: 0; }
  html, body { width: 1200px; height: 514px; overflow: hidden; }
  body {
    position: relative;
    background: var(--backdrop);
    font-family: "Source Sans 3", Arial, sans-serif;
  }
  .postcard {
    position: absolute;
    top: 72px;
    width: 480px;
    height: 370px;
    overflow: hidden;
    box-shadow: 0 2px 6px rgba(0,0,0,.25);
  }
  .postcard--front { left: 86px; }
  .postcard--back { left: 628px; background: var(--white); }

  /* Front: header */
  .front-header {
    position: absolute; left: 0; top: 0; width: 480px; height: 160px;
    background: linear-gradient(180deg, var(--sea-blue) 0%, var(--sea-blue-deep) 100%);
  }
  .brand {
    position: absolute; left: 16px; top: 40px; width: 180px;
    text-align: center;
  }
  .brand__name {
    font-family: "Roboto Condensed", Arial, sans-serif;
    font-weight: 700; font-size: 17px; line-height: 1.15;
    color: var(--white);
  }
  .brand__place {
    margin-top: 6px;
    font-family: "Roboto Condensed", Arial, sans-serif;
    font-size: 11px; color: var(--white);
  }
  .brand__phone {
    display: inline-block; margin-top: 8px; padding: 2px 10px;
    border-radius: 8px; background: var(--gold); color: var(--navy);
    font-family: "Roboto Condensed", Arial, sans-serif; font-weight: 700; font-size: 11px;
  }
  .services {
    position: absolute; left: 210px; top: 21px; list-style: none;
    font-family: "Roboto Condensed", Arial, sans-serif;
    font-size: 12.5px; line-height: 17px; color: var(--white);
  }
  .services li::before { content: "\2022"; margin-right: 5px; }
  .booking {
    position: absolute; left: 252px; top: 115px;
    font-family: "Roboto Condensed", Arial, sans-serif; color: var(--gold);
  }
  .booking__label { font-size: 12.5px; font-weight: 700; padding-left: 6px; }
  .booking__phone {
    display: flex; align-items: center; gap: 5px;
    font-size: 22px; font-weight: 700; line-height: 26px;
  }
  .rope-line {
    position: absolute; left: 0; top: 159px; width: 480px; height: 4px;
    background: repeating-linear-gradient(135deg, var(--rope) 0 3px, #8a6a32 3px 5px);
  }

  /* Front: lower */
  .vessel-panel {
    position: absolute; left: 0; top: 163px; width: 169px; height: 207px;
    background: var(--navy); color: var(--white);
    padding: 24px 10px 0 15px;
    font-family: "PT Sans Narrow", Arial, sans-serif;
    font-weight: 700; font-size: 12px; line-height: 15px;
  }
  .vessel-panel p + p { margin-top: 11px; }
  .front-photo {
    position: absolute; left: 170px; top: 163px; width: 310px; height: 207px;
    background: linear-gradient(180deg, var(--photo-sky) 0%, #cfe2f2 40%, var(--photo-sea) 52%, #e6e9ec 78%, #f2f2f2 100%);
  }

  /* Back */
  .about {
    position: absolute; left: 0; top: 0; width: 252px; height: 370px;
    background: linear-gradient(90deg, #3f66b5 0%, #8aa3d4 22%, #e9eef7 55%, var(--white) 80%);
    padding: 18px 8px 0 16px; color: var(--navy-text);
    display: flex; flex-direction: column;
  }
  .about__title { font-size: 12px; font-weight: 700; line-height: 14px; letter-spacing: .2px; }
  .about__text { margin-top: 7px; font-size: 12px; line-height: 14.5px; }
  .about__text + .about__text { margin-top: 8px; }
  .crew__title {
    margin-top: 10px;
    font-family: "PT Sans Narrow", Arial, sans-serif; font-weight: 700; font-size: 12px; line-height: 14px;
  }
  .crew__list { list-style: none; margin-top: 6px; padding-left: 6px; }
  .crew__list li {
    display: flex; align-items: center; gap: 6px;
    font-family: "PT Sans Narrow", Arial, sans-serif; font-size: 11px; line-height: 14px;
  }
  .payments {
    margin-top: 9px; text-align: center; padding-right: 8px;
  }
  .payments__note {
    font-family: "PT Sans Narrow", Arial, sans-serif; font-weight: 700;
    font-size: 11.5px; line-height: 13px; color: var(--alert-red);
  }
  .card-grid {
    display: grid; grid-template-columns: 34px 34px; gap: 3px;
    width: 71px; margin: 6px auto 0;
  }
  .card-tile {
    height: 21px; border-radius: 2px; border: 1px solid #c8c8c8;
    display: flex; align-items: center; justify-content: center;
    font-size: 11px; font-weight: 700; color: var(--navy-text); background: var(--white);
  }
  .back-photo {
    position: absolute; left: 252px; top: 0; width: 228px; height: 370px;
    background: linear-gradient(180deg, #7fb0e0 0%, #b9cfe3 30%, var(--photo-warm) 60%, #7c6a58 100%);
  }
  .back-booking { position: absolute; left: 290px; top: 322px; }
</style>
</head>
<body>

<section class="postcard postcard--front" aria-label="Postcard front">
  <header class="front-header">
    <div class="brand">
      <div class="brand__name">Harbor Lantern Sport Fishing Charters</div>
      <div class="brand__place">Block Island RI</div>
      <div class="brand__phone">401.555.0193</div>
    </div>
    <ul class="services">
      <li>Shark &amp; Tuna Trips</li>
      <li>Full or half day Inshore Bass &amp; Bluefish</li>
      <li>Half day bottom fishing for Fluke, Sea Bass &amp; Scup</li>
      <li>Inshore night fishing trips</li>
      <li>Custom Combination Charters also available</li>
    </ul>
    <div class="booking">
      <div class="booking__label">For pricing &amp; booking, call:</div>
      <div class="booking__phone">
        <svg width="16" height="16" viewBox="0 0 24 24" aria-hidden="true"><path fill="var(--gold)" d="M6.6 10.8a15 15 0 0 0 6.6 6.6l2.2-2.2c.3-.3.7-.4 1-.2 1.1.4 2.3.6 3.6.6.6 0 1 .4 1 1V20c0 .6-.4 1-1 1C10.6 21 3 13.4 3 4c0-.6.4-1 1-1h3.5c.6 0 1 .4 1 1 0 1.3.2 2.5.6 3.6.1.3 0 .7-.2 1z"/></svg>
        401.555.0193
      </div>
    </div>
  </header>
  <div class="rope-line"></div>
  <div class="vessel-panel">
    <p>The Reel Tide Joy is powered by a twin 250 HP Valdrek Turbo Diesels.</p>
    <p>The boat is fully equipped with all electronics. radar and EPIRB.</p>
    <p>Our sport fishing boat offers a restroom and a galley area with a table so you can enjoy your lunch.</p>
  </div>
  <div class="front-photo" role="img" aria-label="Photo: a parent, a child and a dog sitting on the bow of a sailboat looking out over a blue bay and green hills"></div>
</section>

<section class="postcard postcard--back" aria-label="Postcard back">
  <div class="about">
    <h2 class="about__title">ABOUT REEL TIDE JOY EXPERIENCE</h2>
    <p class="about__text">Captain Dennis Hartwell has been fishing for many years, both commercially and recreational, and is eager to welcome you aboard. The friendly captain and crew will work hard to be sure you have a great day.</p>
    <p class="about__text">Popular catches include Striped Bass, Bluefish, Fluke, Seabass, Albies and offshore big game fish such as Yellowfin Tuna, Bluefin Tuna, Longfin Albacore, White Marlin, Blue Marlin, Dorado, Wahoo, and Sharks.</p>
    <h3 class="crew__title">Our Crew is Dedicated to Provide You with:</h3>
    <ul class="crew__list">
      <li><svg width="12" height="8" viewBox="0 0 12 8" aria-hidden="true"><path d="M0 8 6 0 12 8z" fill="var(--navy-text)"/></svg>A professional and accommodating experience</li>
      <li><svg width="12" height="8" viewBox="0 0 12 8" aria-hidden="true"><path d="M0 8 6 0 12 8z" fill="var(--navy-text)"/></svg>A very child friendly environment</li>
      <li><svg width="12" height="8" viewBox="0 0 12 8" aria-hidden="true"><path d="M0 8 6 0 12 8z" fill="var(--navy-text)"/></svg>A range of technique options for every style of trip</li>
      <li><svg width="12" height="8" viewBox="0 0 12 8" aria-hidden="true"><path d="M0 8 6 0 12 8z" fill="var(--navy-text)"/></svg>An immense knowledge of the waters.</li>
    </ul>
    <div class="payments">
      <p class="payments__note">We except cash , checks and<br>most major credit cards</p>
      <div class="card-grid">
        <div class="card-tile">Kp</div>
        <div class="card-tile">Tz</div>
        <div class="card-tile">Nb</div>
        <div class="card-tile">Rl</div>
      </div>
    </div>
  </div>
  <div class="back-photo" role="img" aria-label="Photo: a child on a boat holding up a freshly caught fluke"></div>
  <div class="booking back-booking">
    <div class="booking__label">For pricing &amp; booking, call:</div>
    <div class="booking__phone">
      <svg width="16" height="16" viewBox="0 0 24 24" aria-hidden="true"><path fill="var(--gold)" d="M6.6 10.8a15 15 0 0 0 6.6 6.6l2.2-2.2c.3-.3.7-.4 1-.2 1.1.4 2.3.6 3.6.6.6 0 1 .4 1 1V20c0 .6-.4 1-1 1C10.6 21 3 13.4 3 4c0-.6.4-1 1-1h3.5c.6 0 1 .4 1 1 0 1.3.2 2.5.6 3.6.1.3 0 .7-.2 1z"/></svg>
      401.555.0193
    </div>
  </div>
</section>

</body>
</html>
```